Calloway Brothers Civil Construction website design

We want a Bold website to promote our Heavy Civil Construction company, We would like an organic / tangible feel to the site. The pictures will be over saturated so they pop. We need to be able to easliy upload new projects and pictures on a regular basis.
Home page will have a full screen width image, "home page image" with silhouette and logo. It will also have about us area and picture
Page 2 will be Project Gallery with pictures in project folders
Page 3 will be an employment application form and submission
Page 4 will be Contact Us
Construction indusrty
Contractor
Coded - Design and coding required
4 page
- Hypatia Sans Pro Light

```html
<!DOCTYPE html>
<html lang="en">
<head>
<meta charset="utf-8">
<title>Calloway Brothers Civil Construction</title>
<link href="https://fonts.googleapis.com/css2?family=Montserrat:wght@400;500;600&family=Poppins:wght@400;500&display=swap" rel="stylesheet">
<style>
:root{
  --blue:#3b50a2;
  --blue-dark:#2e4190;
  --ink:#2b2b2b;
  --text:#3a3a3a;
  --muted:#6b6b6b;
  --panel:#ececec;
  --white:#ffffff;
  --hero-top:#4a4d55;
  --hero-bottom:#8c8f95;
}
*{box-sizing:border-box;margin:0;padding:0}
html,body{width:1200px;height:4395px;overflow:hidden}
body{position:relative;font-family:"Montserrat",sans-serif;color:var(--text);background:var(--white)}
.abs{position:absolute}

/* Hero */
.hero{left:0;top:0;width:1200px;height:680px;background:linear-gradient(180deg,var(--hero-top) 0%,#6d7077 55%,var(--hero-bottom) 75%,#1e1e1e 100%)}
.hero-wave{left:0;top:620px;width:1200px;height:70px}
.brand-small{left:89px;top:38px;display:flex;align-items:center;gap:12px}
.brand-mark{width:30px;height:30px;background:var(--blue)}
.brand-small .brand-name{font-size:17px;font-weight:600;color:#c9d1ee;line-height:1.15;letter-spacing:1px;text-transform:uppercase;width:260px}
.callus{left:622px;top:26px;display:flex;align-items:center;gap:10px;color:var(--white);font-size:14px;line-height:1.45}
.callus svg{width:40px;height:40px}
.callus b{font-weight:600}
.search{left:814px;top:24px;width:296px;height:48px;border-radius:24px;background:var(--white);display:flex;align-items:center;padding:0 6px 0 18px;font-size:16px;color:#8a8a8a}
.search span{flex:1}
.search i{width:36px;height:36px;border-radius:50%;background:var(--blue);display:flex;align-items:center;justify-content:center}
.nav{top:95px;left:0;width:1200px;height:24px;font-size:16px;color:var(--white);font-weight:500}
.nav a{position:absolute;color:inherit;text-decoration:none}
.hero-brand{left:0;top:285px;width:1200px;text-align:center;font-size:46px;font-weight:600;color:#161616;letter-spacing:2px;line-height:1.2;text-transform:uppercase}

/* About */
.photo-ring{border-radius:50%;border:6px solid var(--blue)}
.about-photo{left:80px;top:788px;width:444px;height:444px;background:radial-gradient(circle at 40% 30%,#bfe0f6 0%,#9fc4e2 40%,#e8b23d 62%,#d8d3c8 85%)}
h2.title-mixed{font-size:35px;font-weight:500;color:var(--blue)}
.about-title{left:573px;top:840px}
.body-copy{font-size:14.5px;line-height:34px;text-align:justify;color:var(--text)}
.about-copy{left:573px;top:896px;width:537px}
.btn{display:flex;align-items:center;justify-content:center;gap:8px;background:var(--blue);color:var(--white);font-weight:600;font-size:17px;border-radius:28px}
.btn svg{width:18px;height:18px}
.about-btn{left:573px;top:1118px;width:187px;height:54px}

/* Gallery */
.gallery{left:0;top:1340px;width:1200px;height:1152px;background:var(--panel)}
.section-title{width:1200px;left:0;text-align:center;font-size:32px;font-weight:500;color:var(--blue);text-transform:uppercase}
.gallery-title{top:1440px}
.tile{position:absolute}
.t1{left:77px;top:1528px;width:508px;height:278px;background:linear-gradient(180deg,#f3f1ea 0%,#d6d6d0 55%,#7d7b72 100%)}
.t2{left:604px;top:1528px;width:521px;height:513px;background:linear-gradient(135deg,#d9c89a 0%,#e9dfc1 45%,#c2a878 100%)}
.t3{left:77px;top:1828px;width:244px;height:446px;background:linear-gradient(180deg,#9aa689 0%,#dadcd7 35%,#e88b3f 70%,#6f6a60 100%)}
.t4{left:341px;top:1828px;width:244px;height:213px;background:linear-gradient(160deg,#f0a13b 0%,#b8542a 55%,#3d2a20 100%)}
.t5{left:341px;top:2062px;width:244px;height:212px;background:linear-gradient(180deg,#c3c0ae 0%,#a7925c 55%,#6d5a36 100%)}
.t6{left:604px;top:2062px;width:251px;height:212px;background:linear-gradient(180deg,#cfcfca 0%,#b6b2a6 55%,#5c5850 100%)}
.t7{left:872px;top:2062px;width:253px;height:212px;background:linear-gradient(160deg,#7f7f82 0%,#c9a53e 50%,#5b5b5e 100%)}
.gallery-btn{left:474px;top:2330px;width:251px;height:55px;font-size:16px}

/* Employment */
.employ{left:0;top:2492px;width:1200px;height:666px;background:linear-gradient(180deg,#f4f6f8 0%,#f1ede6 60%,#c9c6c1 100%)}
.employ-title{left:90px;top:2658px}
.employ-copy{left:90px;top:2714px;width:536px}
.employ-btn{left:89px;top:2931px;width:189px;height:55px}
.employ-photo{left:674px;top:2603px;width:444px;height:444px;background:radial-gradient(circle at 60% 40%,#e2b79c 0%,#e9e2da 45%,#cfd3d8 100%)}

/* Contact */
.contact{left:0;top:3158px;width:1200px;height:887px;background:var(--panel)}
.contact-title{top:3262px}
.contact-sub{left:0;top:3316px;width:1200px;text-align:center;font-size:21px;color:var(--muted)}
.info{width:300px;text-align:center;font-size:16px;line-height:29px;color:var(--muted)}
.info .dot{width:86px;height:86px;border-radius:50%;background:var(--blue);margin:0 auto 18px;display:flex;align-items:center;justify-content:center}
.info .dot svg{width:44px;height:44px}
.form-title{top:3588px}
.field{background:var(--white);height:34px;display:flex;align-items:center;gap:6px;padding-left:16px;font-family:"Poppins",sans-serif;font-size:11px;color:#555}
.field svg{width:10px;height:10px}
.field.area{align-items:flex-start;padding-top:10px}
.submit{left:512px;top:3871px;width:178px;height:50px;background:var(--blue);color:var(--white);display:flex;align-items:center;justify-content:center;gap:10px;font-size:17px;font-weight:600}
.submit svg{width:20px;height:20px}

/* Footer */
.footer{left:0;top:4045px;width:1200px;height:350px;background:linear-gradient(180deg,#ffffff 0%,#d6d6d6 30%,#9a9a9a 75%,#2b2b2b 100%)}
.footer-wave{left:0;top:4030px;width:1200px;height:40px}
.footer-brand{left:0;top:4130px;width:1200px;display:flex;justify-content:center;align-items:center;gap:12px}
.footer-brand .brand-mark{background:var(--ink);width:34px;height:34px}
.footer-brand .brand-name{font-size:22px;font-weight:600;color:var(--ink);line-height:1.1;text-transform:uppercase;letter-spacing:1px;width:290px}
.footer-links{left:0;top:4210px;width:1200px;text-align:center;font-size:15.5px;color:var(--ink)}
.footer-links span{margin:0 8px}
.copyright{left:0;top:4245px;width:1200px;text-align:center;font-size:15px;color:var(--ink)}
.social{left:532px;top:4284px;display:flex;gap:8px}
.social i{width:28px;height:28px;border-radius:50%;border:2px solid var(--ink)}
</style>
</head>
<body>

<!-- Hero -->
<div class="abs hero" role="img" aria-label="Dusk sky over a construction site with silhouetted excavator and dump trucks"></div>
<svg class="abs hero-wave" viewBox="0 0 1200 70" preserveAspectRatio="none" aria-hidden="true">
  <path d="M0 35 Q30 5 60 35 T120 35 T180 35 T240 35 T300 35 T360 35 T420 35 T480 35 T540 35 T600 35 T660 35 T720 35 T780 35 T840 35 T900 35 T960 35 T1020 35 T1080 35 T1140 35 T1200 35 L1200 70 L0 70Z" fill="#ffffff"/>
</svg>
<div class="abs brand-small"><div class="brand-mark"></div><div class="brand-name">Calloway Brothers Civil Construction</div></div>
<div class="abs callus">
  <svg viewBox="0 0 40 40"><circle cx="20" cy="20" r="18" fill="none" stroke="#fff" stroke-width="2.5"/><path d="M13 11l4 0 2 5-2.5 2a12 12 0 0 0 6 6l2-2.5 5 2 0 4a2 2 0 0 1-2 2A17 17 0 0 1 11 13a2 2 0 0 1 2-2z" fill="#fff"/></svg>
  <div><b>Call us:</b><br>(888) 888-8888</div>
</div>
<div class="abs search"><span>Search</span><i><svg width="14" height="14" viewBox="0 0 14 14"><circle cx="6" cy="6" r="4" fill="none" stroke="#fff" stroke-width="2"/><path d="M9 9l3.5 3.5" stroke="#fff" stroke-width="2"/></svg></i></div>
<nav class="abs nav">
  <a style="left:435px">Home</a>
  <a style="left:527px">About Us</a>
  <a style="left:647px">Project Gallery</a>
  <a style="left:807px">Employee Application</a>
  <a style="left:1024px">Contact Us</a>
</nav>
<div class="abs hero-brand">Calloway Brothers<br>Civil Construction</div>

<!-- About -->
<div class="abs photo-ring about-photo" role="img" aria-label="Yellow hard hat and safety gear on a desk with a city skyline behind"></div>
<h2 class="abs title-mixed about-title">About Us</h2>
<p class="abs body-copy about-copy">Sed ut perspiciatis unde omnis iste natus error sit voluptatem accusantium doloremque laudantium, totam rem aperiam, eaque ipsa quae ab illo inventore veritatis et quasi architecto beatae vitae dicta sunt explicabo. Nemo enim ipsam voluptatem quia voluptas sit aspernatur aut odit aut fugit, sed quia consequuntur magni dolores eos qui ratione voluptatem sequi nesciunt.</p>
<div class="abs btn about-btn">Read More <svg viewBox="0 0 18 18"><circle cx="9" cy="9" r="8" fill="#fff"/><path d="M5 9h7M9 5.5 12.5 9 9 12.5" stroke="#3b50a2" stroke-width="2" fill="none"/></svg></div>

<!-- Gallery -->
<section class="abs gallery"></section>
<h2 class="abs section-title gallery-title">Project Gallery</h2>
<div class="tile t1" role="img" aria-label="High-rise under construction with tower cranes"></div>
<div class="tile t2" role="img" aria-label="Hands reviewing rolled construction plans on a desk"></div>
<div class="tile t3" role="img" aria-label="Site engineer in hard hat and safety vest holding plans"></div>
<div class="tile t4" role="img" aria-label="Welder at work with sparks against a sunset skyline"></div>
<div class="tile t5" role="img" aria-label="Road grader and loader on a dirt site"></div>
<div class="tile t6" role="img" aria-label="Engineer with clipboard beneath a concrete bridge"></div>
<div class="tile t7" role="img" aria-label="Aerial view of a backhoe and road crew at work"></div>
<div class="abs btn gallery-btn">View the entire gallery <svg viewBox="0 0 18 18"><circle cx="9" cy="9" r="8" fill="#fff"/><path d="M5 9h7M9 5.5 12.5 9 9 12.5" stroke="#3b50a2" stroke-width="2" fill="none"/></svg></div>

<!-- Employment -->
<section class="abs employ" role="img" aria-label="Pale morning sky over faint construction machinery silhouettes"></section>
<h2 class="abs title-mixed employ-title">Employee Application</h2>
<p class="abs body-copy employ-copy">Sed ut perspiciatis unde omnis iste natus error sit voluptatem accusantium doloremque laudantium, totam rem aperiam, eaque ipsa quae ab illo inventore veritatis et quasi architecto beatae vitae dicta sunt explicabo. Nemo enim ipsam voluptatem quia voluptas sit aspernatur aut odit aut fugit, sed quia consequuntur magni dolores eos qui ratione voluptatem sequi nesciunt.</p>
<div class="abs btn employ-btn">Apply Now <svg viewBox="0 0 18 18"><circle cx="9" cy="9" r="8" fill="#fff"/><path d="M5 9h7M9 5.5 12.5 9 9 12.5" stroke="#3b50a2" stroke-width="2" fill="none"/></svg></div>
<div class="abs photo-ring employ-photo" role="img" aria-label="Hand with a pen filling out a paper form"></div>

<!-- Contact -->
<section class="abs contact"></section>
<h2 class="abs section-title contact-title">Contact Information</h2>
<p class="abs contact-sub">Contact us for more information</p>
<div class="abs info" style="left:144px;top:3376px">
  <div class="dot"><svg viewBox="0 0 44 44"><path d="M22 6a10 10 0 0 0-10 10c0 8 10 18 10 18s10-10 10-18A10 10 0 0 0 22 6z" fill="none" stroke="#fff" stroke-width="2"/><circle cx="22" cy="16" r="4" fill="none" stroke="#fff" stroke-width="2"/><path d="M12 38h20" stroke="#fff" stroke-width="2"/></svg></div>
  418 Harbor Lane - Suite B,<br>Westfield, FL 30010
</div>
<div class="abs info" style="left:434px;top:3376px">
  <div class="dot"><svg viewBox="0 0 44 44"><path d="M12 8l7 0 3 8-4 3a18 18 0 0 0 8 8l3-4 8 3 0 7a3 3 0 0 1-3 3A27 27 0 0 1 9 11a3 3 0 0 1 3-3z" fill="none" stroke="#fff" stroke-width="2"/></svg></div>
  Phone:<br>+1 888 888 8888
</div>
<div class="abs info" style="left:755px;top:3376px">
  <div class="dot"><svg viewBox="0 0 44 44"><rect x="8" y="12" width="28" height="20" fill="none" stroke="#fff" stroke-width="2"/><path d="M8 12l14 11 14-11M8 32l11-10M36 32 25 22" fill="none" stroke="#fff" stroke-width="2"/></svg></div>
  Email:<br>info@company.com
</div>

<h2 class="abs section-title form-title">Contact Form</h2>
<div class="abs field" style="left:164px;top:3658px;width:427px"><svg viewBox="0 0 10 10"><circle cx="5" cy="3" r="2.2" fill="#555"/><path d="M1 10a4 4 0 0 1 8 0z" fill="#555"/></svg>First Name</div>
<div class="abs field" style="left:611px;top:3658px;width:427px"><svg viewBox="0 0 10 10"><circle cx="5" cy="3" r="2.2" fill="#555"/><path d="M1 10a4 4 0 0 1 8 0z" fill="#555"/></svg>Last Name</div>
<div class="abs field" style="left:164px;top:3713px;width:427px"><svg viewBox="0 0 10 10"><rect x="2" y="1" width="6" height="9" fill="#555"/></svg>Company</div>
<div class="abs field" style="left:164px;top:3767px;width:427px"><svg viewBox="0 0 10 10"><rect x="1" y="2" width="8" height="6" fill="none" stroke="#555"/><path d="M1 2l4 3 4-3" fill="none" stroke="#555"/></svg>Email Address</div>
<div class="abs field" style="left:164px;top:3822px;width:427px"><svg viewBox="0 0 10 10"><path d="M2 1h2l1 2-1.2 1a5 5 0 0 0 2.2 2.2L7 5l2 1v2a1 1 0 0 1-1 1A7 7 0 0 1 1 2a1 1 0 0 1 1-1z" fill="#555"/></svg>Phone Number</div>
<div class="abs field area" style="left:611px;top:3713px;width:427px;height:145px"><svg viewBox="0 0 10 10"><ellipse cx="5" cy="4.5" rx="4.5" ry="3.3" fill="#555"/></svg>Message :</div>
<div class="abs submit"><svg viewBox="0 0 20 20"><path d="M2 10 18 3 14 17 10 12z" fill="#fff"/></svg>Submit</div>

<!-- Footer -->
<footer class="abs footer" role="img" aria-label="Grey sky with silhouetted excavators and trucks along the ground"></footer>
<svg class="abs footer-wave" viewBox="0 0 1200 40" preserveAspectRatio="none" aria-hidden="true">
  <path d="M0 20 Q15 8 30 20 T60 20 T90 20 T120 20 T150 20 T180 20 T210 20 T240 20 T270 20 T300 20 T330 20 T360 20 T390 20 T420 20 T450 20 T480 20 T510 20 T540 20 T570 20 T600 20 T630 20 T660 20 T690 20 T720 20 T750 20 T780 20 T810 20 T840 20 T870 20 T900 20 T930 20 T960 20 T990 20 T1020 20 T1050 20 T1080 20 T1110 20 T1140 20 T1170 20 T1200 20" fill="none" stroke="#3b50a2" stroke-width="5"/>
</svg>
<div class="abs footer-brand"><div class="brand-mark"></div><div class="brand-name">Calloway Brothers Civil Construction</div></div>
<div class="abs footer-links">Home<span>|</span>About Us<span>|</span>Project Gallery<span>|</span>Employee Application<span>|</span>Contact Us</div>
<div class="abs copyright">© 2019 Company Name All right reserved</div>
<div class="abs social"><i></i><i></i><i></i><i></i></div>

</body>
</html>
```